Brisa Lumen Systems Corp Business Cards

Business cards to match the logo.

Company is a start up water technology company that has developed a patented system using centrifugal force to separate waste from municipal waste water to produce crystal clear clean water. Product sell starting at 2 million to governments both in the US and international.

Business cards should have a professional look with the target generally engineers.

Target Market(s)

Engineers, Government officials and investors

Industry/Entity Type

Water Treatment

Contact Information for Business Card

Business cards design will be used for 6 to 8 people with job titles. Can use the quote "If there is magic in the planet, it is contained in water." but not required to use quote. Should follow theme of Logo

Font styles to use
Other font styles liked:
• match logo font

Requirements
Nice to have
• Colors to match Logo. Business cards to match style of flow of Logo.
• Emphasis on clean look not a busy look. Clean flowing water.
Should not have
• Pictures of industrial equipment or wastewater

```html
<!DOCTYPE html>
<html lang="en">
<head>
<meta charset="utf-8">
<title>Brisa Lumen Systems Corp — Business Cards</title>
<link rel="stylesheet" href="https://fonts.googleapis.com/css2?family=Arimo:wght@400&family=Tinos:wght@400;700&display=swap">
<style>
  :root {
    --backdrop: #4b423d;
    --card: #0d0d0e;
    --card-edge: #1b1b1c;
    --brand-blue: #1f8fd0;
    --name-blue: #27a6e6;
    --silver: #d6d8da;
    --text-light: #e8e8e8;
    --divider: #3a3a3c;
  }
  * { box-sizing: border-box; margin: 0; padding: 0; }
  html, body {
    width: 1200px; height: 844px; overflow: hidden;
    background: var(--backdrop);
  }
  .sheet {
    position: relative; width: 1200px; height: 844px;
    display: flex; align-items: center; justify-content: center; gap: 60px;
  }
  .card {
    width: 500px; height: 286px;
    background: var(--card);
    border: 1px solid var(--card-edge);
    box-shadow: 0 14px 30px rgba(0,0,0,.45);
    position: relative;
  }
  /* Back: logo and contact details */
  .card-back { display: flex; }
  .brand-panel {
    width: 54%; display: flex; align-items: center; justify-content: center;
    border-right: 1px solid var(--divider);
    margin: 34px 0;
  }
  .wordmark {
    font-family: "Tinos", serif; font-weight: 400;
    text-transform: uppercase; text-align: center; line-height: 1.1;
  }
  .wordmark-back { color: var(--brand-blue); font-size: 27px; letter-spacing: 1px; }
  .wordmark-back .line-2 { font-size: 15px; letter-spacing: 7px; }
  .contact-panel {
    flex: 1; padding: 48px 0 0 22px; color: var(--text-light);
    font-family: "Arimo", sans-serif; font-size: 13px; line-height: 1.3;
  }
  .person-name {
    font-family: "Tinos", serif; font-weight: 700; font-size: 16px;
    color: var(--name-blue); text-transform: uppercase; letter-spacing: .5px;
  }
  .person-title { margin-bottom: 6px; }
  .contact-list { list-style: none; }
  .contact-list li { display: flex; align-items: center; gap: 7px; }
  .contact-list svg { width: 10px; height: 10px; fill: var(--name-blue); flex: none; }
  .address { margin-top: 10px; }
  /* Front: logo only */
  .card-front { display: flex; align-items: center; justify-content: center; }
  .wordmark-front { color: var(--silver); font-size: 40px; letter-spacing: 1px; }
  .wordmark-front .line-2 { font-size: 21px; letter-spacing: 11px; }
</style>
</head>
<body>
<main class="sheet">
  <section class="card card-back" aria-label="Business card back">
    <div class="brand-panel">
      <p class="wordmark wordmark-back"><span>Brisa Lumen</span><br><span class="line-2">Systems</span></p>
    </div>
    <div class="contact-panel">
      <h1 class="person-name">Marcus Hale</h1>
      <p class="person-title">Managing Director</p>
      <ul class="contact-list">
        <li><svg viewBox="0 0 10 10" aria-hidden="true"><path d="M1 3c0-2 2-2 2-2l1 2-1 1c1 2 2 3 3 3l1-1 2 1s0 2-2 2C4 9 1 6 1 3z"/></svg>044-210 555 017</li>
        <li><svg viewBox="0 0 10 10" aria-hidden="true"><path d="M3 0h4a1 1 0 0 1 1 1v8a1 1 0 0 1-1 1H3a1 1 0 0 1-1-1V1a1 1 0 0 1 1-1zm0 1.5v6h4v-6z"/></svg>044-210 555 018</li>
        <li><svg viewBox="0 0 10 10" aria-hidden="true"><path d="M0 2h10v6H0zm1 1v.3l4 2.5 4-2.5V3z"/></svg>info@brisalumen.example</li>
        <li><svg viewBox="0 0 10 10" aria-hidden="true"><circle cx="5" cy="5" r="5"/></svg>www.brisalumen.example</li>
      </ul>
      <p class="address">48 Harbor Lane, Portvale<br>Country Name, 20817.</p>
    </div>
  </section>
  <section class="card card-front" aria-label="Business card front">
    <p class="wordmark wordmark-front"><span>Brisa Lumen</span><br><span class="line-2">Systems</span></p>
  </section>
</main>
</body>
</html>
```